Business incubator; Angel investments; Consulting for startups

We need new office equipment

Target Market(s)

Start up Company

Font styles to use
Sans Serif

Colors

Designer to choose only greyscale colors for use in the design.

Requirements
Must have
• Existing company logo
Nice to have
• Corporate according to the website www.twm-norvane.com
Should not have
• Colors off gray

```html
<!DOCTYPE html>
<html lang="en">
<head>
<meta charset="utf-8">
<title>TWM Norvane – Stationery</title>
<link href="https://fonts.googleapis.com/css2?family=Roboto:wght@400;500;700&display=swap" rel="stylesheet">
<style>
:root{
  --bg:#eeeef0;
  --paper:#ffffff;
  --ink:#5f5d5e;
  --ink-soft:#8a8889;
  --ghost:#f3f3f3;
  --line:#dcdcdc;
}
*{margin:0;padding:0;box-sizing:border-box}
html,body{width:1200px;height:795px;overflow:hidden;background:var(--bg);font-family:'Roboto',sans-serif;color:var(--ink)}
.canvas{position:relative;width:1200px;height:795px}
.sheet{position:absolute;background:var(--paper);box-shadow:0 1px 3px rgba(0,0,0,.12);overflow:hidden}
.brand{font-weight:700;color:var(--ink);display:flex;align-items:center;gap:4px;letter-spacing:.5px}
.brand .dot{border-radius:50%;background:var(--ink);display:inline-block}
.ghost-name{position:absolute;font-weight:700;color:var(--ghost);letter-spacing:4px}

/* letterhead */
.letterhead{left:292px;top:100px;width:294px;height:414px}
.letterhead .brand{position:absolute;right:28px;top:48px;font-size:17px}
.letterhead .brand .dot{width:8px;height:8px}
.letterhead .ghost-name{left:60px;top:190px;font-size:90px}
.letter-body{position:absolute;left:19px;top:106px;width:256px;font-size:4.6px;line-height:1.45;color:var(--ink-soft)}
.letter-body p{margin-bottom:6px;text-align:justify}
.letter-body .strong{font-weight:700;color:var(--ink)}
.signature{width:66px;height:12px;background:linear-gradient(90deg,#e8e8ee,#f4f4f7);margin:4px 0 3px}
.letter-foot{position:absolute;left:0;bottom:0;width:294px;height:70px}
.letter-foot .company{position:absolute;left:19px;top:12px;font-size:7px;font-weight:700}
.letter-foot .contacts{position:absolute;right:10px;bottom:9px;text-align:right;color:#fff;font-size:4.8px;line-height:1.6}

/* folder */
.folder{left:635px;top:80px;width:345px;height:436px}
.folder .edge{position:absolute;top:0;bottom:0;width:1px;background:var(--line)}
.folder .brand{position:absolute;left:128px;top:196px;font-size:34px}
.folder .brand .dot{width:14px;height:14px}

/* cards */
.card-front{left:186px;top:550px;width:132px;height:76px;background:var(--ink)}
.card-front .brand{position:absolute;left:38px;top:28px;font-size:15px;color:#fff}
.card-front .brand .dot{width:6px;height:6px;background:#fff}
.card-back{left:186px;top:646px;width:132px;height:77px}
.card-back .brand{position:absolute;left:16px;top:21px;font-size:11px}
.card-back .brand .dot{width:5px;height:5px}
.card-back .person{position:absolute;right:7px;top:11px;text-align:right;font-size:4.4px;color:var(--ink-soft)}
.card-back .person b{display:block;font-size:5px;color:var(--ink)}
.card-back svg{position:absolute;left:0;bottom:0}
.card-back .contacts{position:absolute;right:7px;bottom:5px;text-align:right;color:#fff;font-size:3.4px;line-height:1.55}

/* envelopes */
.envelope-front{left:353px;top:561px;width:349px;height:157px}
.envelope-front .brand{position:absolute;left:18px;top:25px;font-size:13px}
.envelope-front .brand .dot{width:5px;height:5px}
.envelope-front .address{position:absolute;left:75px;top:42px;font-size:5px;color:var(--ink-soft)}
.envelope-front .address b{display:block;font-size:6.4px;color:var(--ink);margin-bottom:3px}
.envelope-front .ghost-name{left:210px;top:80px;font-size:40px}
.envelope-back{left:710px;top:561px;width:350px;height:157px}
.envelope-back svg{position:absolute;left:0;top:0}
.envelope-back .web{position:absolute;left:0;width:100%;top:26px;text-align:center;color:#fff;font-size:5px;letter-spacing:2px}
</style>
</head>
<body>
<main class="canvas">

  <section class="sheet letterhead">
    <div class="ghost-name">TWM</div>
    <div class="brand"><span class="dot"></span>TWM</div>
    <div class="letter-body">
      <p>30/20/2016</p>
      <p><span class="strong">Mr. XYZ Smith</span><br>123, Street No. 123,<br>City Name<br>Pincode-123456</p>
      <p>Dear Sir,</p>
      <p>Our team supports early founders with practical guidance, shared workspace and patient capital. We help each venture shape a clear plan, test its market and build a steady path toward growth, while keeping costs low and decisions simple for everyone involved from the very first day.</p>
      <p>Our team supports early founders with practical guidance, shared workspace and patient capital. We help each venture shape a clear plan, test its market and build a steady path toward growth, while keeping costs low and decisions simple for everyone involved from the very first day.</p>
      <p>We look forward to meeting you and learning more about your ideas and plans.</p>
      <p style="margin-top:22px;margin-bottom:0"><span class="strong">Your Name</span></p>
      <div class="signature" role="img" aria-label="Handwritten signature"></div>
      <p>CEO | Owner</p>
    </div>
    <div class="letter-foot">
      <svg width="294" height="70" viewBox="0 0 294 70">
        <path d="M0 48 C70 22 170 12 294 22 L294 70 L0 70 Z" fill="#e7e7e7"/>
        <path d="M0 55 C80 30 180 20 294 28 L294 70 L0 70 Z" fill="var(--ink)"/>
        <path d="M0 62 C70 48 110 52 150 58 L150 70 L0 70 Z" fill="#fff"/>
        <path d="M0 66 C70 54 110 58 150 64 L150 70 L0 70 Z" fill="var(--ink)"/>
      </svg>
      <div class="company">TWM NORVANE PLC</div>
      <div class="contacts">
        +44 (0) 203 000 4821 &#9742;<br>
        info@twm-norvane.com &#9679; twm-norvane.com &#9679;<br>
        2nd Floor, 48 Harbour Lane London E1 7QA, UK &#9906;
      </div>
    </div>
  </section>

  <section class="sheet folder">
    <span class="edge" style="left:12px"></span>
    <span class="edge" style="left:20px"></span>
    <div class="brand"><span class="dot"></span>TWM</div>
  </section>

  <section class="sheet card-front">
    <div class="brand"><span class="dot"></span>TWM</div>
  </section>

  <section class="sheet card-back">
    <div class="brand"><span class="dot"></span>TWM</div>
    <div class="person"><b>Tomas Lindqvist</b>Chief Operating Officer</div>
    <svg width="132" height="44" viewBox="0 0 132 44">
      <path d="M0 30 C30 10 70 2 132 6 L132 44 L0 44 Z" fill="var(--ink)"/>
      <path d="M0 36 C25 24 45 30 62 36 L62 44 L0 44 Z" fill="#fff"/>
      <path d="M0 40 C25 30 45 35 62 40 L62 44 L0 44 Z" fill="var(--ink)"/>
    </svg>
    <div class="contacts">
      +44 (0) 203 000 4821 &#9742;<br>
      +44 (0) 7700 900 316 &#9742;<br>
      www.twm-norvane.com &#9679;<br>
      t.lindqvist@twm-norvane.com &#9679;
    </div>
  </section>

  <section class="sheet envelope-front">
    <div class="ghost-name">TWM</div>
    <div class="brand"><span class="dot"></span>TWM</div>
    <div class="address"><b>TWM NORVANE PLC</b>2nd Floor, 48 Harbour Lane London E1 7QA, UK</div>
  </section>

  <section class="sheet envelope-back">
    <svg width="350" height="157" viewBox="0 0 350 157">
      <path d="M0 0 L350 0 L322 44 Q318 52 308 52 L42 52 Q32 52 28 44 Z" fill="var(--ink)"/>
    </svg>
    <div class="web">www.twm-norvane.com</div>
  </section>

</main>
</body>
</html>
```